Corvane semiconductor corporate presentation

We need a new template with some fresh design elements as we've just announced the acquisition of a new company. Similarly, the backend of the ppt is not set up correctly - and doesn't format properly when dropping in copied text. Attached is the powerpoint presentation/ template as it stands today.
Industry/Entity Type
It Company
Font styles to use
Other font styles liked:
- Arial
Look and feel
Each slider illustrates characteristics of the customer's brand and the style your logo design should communicate.

```html
<!DOCTYPE html>
<html lang="en">
<head>
<meta charset="utf-8">
<title>Corvane semiconductor – presentation template</title>
<link href="https://fonts.googleapis.com/css2?family=Raleway:wght@300;400;600;700&display=swap" rel="stylesheet">
<style>
:root{
  --teal:#1aa9cc;
  --teal-deep:#1590a8;
  --teal-soft:#bfe6f0;
  --purple:#8b2a8d;
  --green:#8dc74b;
  --pink:#e5257d;
  --ink:#3d4a52;
  --grey:#9aa5ab;
  --rule:#e3e8ea;
  --partner:#1f5b3a;
  --white:#fff;
}
*{margin:0;padding:0;box-sizing:border-box}
html,body{width:711px;height:1200px;overflow:hidden;background:var(--white)}
body{font-family:"Raleway",Arial,sans-serif;color:var(--ink)}
.deck{display:grid;grid-template-columns:repeat(3,231px);grid-auto-rows:163px;gap:8px 6px;padding:4px 3px}
.slide{position:relative;overflow:hidden;background:var(--white);box-shadow:0 0 0 .6px #dfe3e5,0 1px 3px rgba(0,0,0,.12)}
.abs{position:absolute}
.photo{position:absolute}
.head{position:absolute;left:9px;top:6px;font-weight:300;font-size:9.5px;color:var(--teal)}
.head::after{content:"";position:absolute;left:0;top:15px;width:213px;height:.6px;background:var(--rule)}
.head.white{color:var(--white)}
.head.white::after{background:rgba(255,255,255,.35)}
.tiny{font-size:3.2px;line-height:1.45;color:var(--grey)}
.tiny.w{color:rgba(255,255,255,.9)}
.tiny.t{color:var(--teal)}
.foot{position:absolute;left:8px;right:8px;bottom:7px;height:6px}
.foot::before{content:"";position:absolute;left:8px;right:10px;top:2px;height:.5px;background:var(--teal-soft)}
.foot .dot{position:absolute;left:0;top:0;width:5px;height:5px;border-radius:50%;background:var(--teal)}
.foot .sq{position:absolute;right:0;top:0;width:5px;height:5px;background:var(--partner)}
.foot .copy{position:absolute;right:12px;top:3px;font-size:2.4px;color:var(--grey)}
.brand{position:absolute;display:flex;align-items:center;gap:3px;font-weight:600;white-space:nowrap}
.brand .c{border-radius:50%;background:currentColor}
.brand .s{background:currentColor}
.title-caps{position:absolute;font-weight:700;text-transform:uppercase;letter-spacing:.2px}
.sub{position:absolute;font-size:3.6px}
.circle-ico{position:absolute;border-radius:50%;display:flex;align-items:center;justify-content:center}
</style>
</head>
<body>
<main class="deck">

  <!-- 1 cover with photo -->
  <section class="slide">
    <div class="photo" style="inset:0;background:linear-gradient(130deg,#19a4cc 0%,#34b7b6 38%,#c69757 68%,#5b3f33 100%)" role="img" aria-label="Concert crowd photographing a stage with a phone"></div>
    <div class="brand" style="left:9px;top:9px;color:var(--white);font-size:10px"><span class="c" style="width:7px;height:7px"></span>Corvane</div>
    <div class="title-caps" style="left:9px;top:117px;color:var(--white);font-size:13.5px">Your Title Goes Here</div>
    <div class="sub" style="left:9px;top:136px;color:var(--white)">Your Subtitle Goes Here</div>
  </section>

  <!-- 2 cover with portrait -->
  <section class="slide">
    <div class="photo" style="left:95px;top:0;right:0;height:150px;background:linear-gradient(90deg,#fff 0%,#d9dde0 30%,#9ea7ad 70%,#c9cfd3 100%)" role="img" aria-label="Smiling engineer working at a laptop"></div>
    <div class="brand" style="left:9px;top:28px;color:var(--teal);font-size:10px"><span class="c" style="width:7px;height:7px"></span>Corvane</div>
    <div class="brand" style="left:74px;top:29px;color:var(--partner);font-size:6px"><span class="s" style="width:7px;height:9px"></span>VELMARK</div>
    <div class="title-caps" style="left:9px;top:116px;color:var(--teal);font-size:13.5px">Your Title Goes Here</div>
    <div class="sub" style="left:9px;top:134px;color:var(--teal)">Your Subtitle Goes Here</div>
    <div class="tiny" style="position:absolute;left:93px;top:151px;font-size:2.4px">© 2017 Corvane Semiconductor</div>
  </section>

  <!-- 3 cover with purple band -->
  <section class="slide">
    <svg class="abs" style="left:0;top:63px" width="82" height="18" viewBox="0 0 82 18"><polygon points="0,0 82,0 74,18 0,18" fill="var(--purple)"/></svg>
    <div class="brand" style="left:96px;top:66px;color:var(--teal);font-size:10px"><span class="c" style="width:7px;height:7px"></span>Corvane</div>
    <div class="brand" style="left:168px;top:67px;color:var(--partner);font-size:6px"><span class="s" style="width:7px;height:9px"></span>VELMARK</div>
    <div class="abs" style="right:9px;top:104px;color:var(--teal);font-size:11.5px;font-weight:600">Your Title Goes Here</div>
    <div class="sub" style="right:9px;top:119px;color:var(--teal)">Your Subtitle Goes Here</div>
  </section>

  <!-- 4 centred cover -->
  <section class="slide">
    <div class="brand" style="left:36px;top:55px;color:var(--teal);font-size:17px"><span class="c" style="width:11px;height:11px"></span>Corvane</div>
    <div class="abs" style="left:134px;top:54px;width:.6px;height:24px;background:var(--rule)"></div>
    <div class="brand" style="left:144px;top:58px;color:var(--partner);font-size:8px"><span class="s" style="width:9px;height:13px"></span>VELMARK</div>
    <div class="abs" style="left:0;right:0;top:104px;height:1px;background:var(--purple)"></div>
    <div class="abs" style="left:0;right:0;top:115px;text-align:center;color:var(--teal);font-size:12px;font-weight:600">Your Title Goes Here</div>
    <div class="sub" style="left:0;right:0;top:131px;text-align:center;color:var(--teal)">Your Subtitle Goes Here</div>
  </section>

  <!-- 5 diagonal cover -->
  <section class="slide">
    <div class="photo" style="inset:0;background:linear-gradient(135deg,#1f9fb8,#1b8ea6 60%,#2ba3a6)" role="img" aria-label="Teal circuit board close-up"></div>
    <svg class="abs" style="left:0;top:0" width="231" height="163" viewBox="0 0 231 163">
      <polygon points="0,0 150,0 0,125" fill="var(--white)"/>
      <line x1="175" y1="0" x2="10" y2="163" stroke="var(--green)" stroke-width="1"/>
    </svg>
    <div class="brand" style="left:7px;top:29px;color:var(--ink);font-size:3px;font-weight:400"><span class="s" style="width:5px;height:5px;background:var(--grey)"></span>the velmark group</div>
    <div class="title-caps" style="left:53px;top:86px;color:var(--white);font-size:11.5px">Your Title Goes Here</div>
    <div class="sub" style="right:30px;top:102px;color:var(--white)">Your Subtitle Goes Here</div>
  </section>

  <!-- 6 agenda -->
  <section class="slide">
    <div class="head">Our Agenda</div>
    <div class="abs" style="left:34px;top:43px;width:180px">
      <div style="display:grid;grid-template-columns:1fr 1fr;row-gap:14px;column-gap:14px">
        <div style="display:flex;gap:4px"><span class="circle-ico" style="position:static;width:8px;height:8px;border:1px solid var(--teal)"></span><div><div style="font-size:4px;color:var(--teal)">Agenda One</div><div class="tiny" style="width:58px">Brief note on the topic and the key points for review.</div></div></div>
        <div style="display:flex;gap:4px"><span class="circle-ico" style="position:static;width:8px;height:8px;border:1px solid var(--teal)"></span><div><div style="font-size:4px;color:var(--teal)">Agenda Four</div><div class="tiny" style="width:58px">Brief note on the topic and the key points for review.</div></div></div>
        <div style="display:flex;gap:4px"><span class="circle-ico" style="position:static;width:8px;height:8px;border:1px solid var(--teal)"></span><div><div style="font-size:4px;color:var(--teal)">Agenda Two</div><div class="tiny" style="width:58px">Brief note on the topic and the key points for review.</div></div></div>
        <div style="display:flex;gap:4px"><span class="circle-ico" style="position:static;width:8px;height:8px;border:1px solid var(--teal)"></span><div><div style="font-size:4px;color:var(--teal)">Agenda Five</div><div class="tiny" style="width:58px">Brief note on the topic and the key points for review.</div></div></div>
        <div style="display:flex;gap:4px"><span class="circle-ico" style="position:static;width:8px;height:8px;border:1px solid var(--teal)"></span><div><div style="font-size:4px;color:var(--teal)">Agenda Three</div><div class="tiny" style="width:58px">Brief note on the topic and the key points for review.</div></div></div>
        <div style="display:flex;gap:4px"><span class="circle-ico" style="position:static;width:8px;height:8px;border:1px solid var(--teal)"></span><div><div style="font-size:4px;color:var(--teal)">Agenda Six</div><div class="tiny" style="width:58px">Brief note on the topic and the key points for review.</div></div></div>
      </div>
    </div>
    <div class="foot"><span class="dot"></span><span class="copy">© 2017 Corvane Semiconductor. All rights reserved</span><span class="sq"></span></div>
  </section>

  <!-- 7 title and image + text -->
  <section class="slide">
    <div class="head">Title And Image + Text</div>
    <div class="photo" style="left:9px;top:33px;width:109px;height:55px;background:linear-gradient(90deg,#f2f4f5,#cfd6da 50%,#8fa2ad)" role="img" aria-label="Businessman in a suit"></div>
    <div class="abs" style="left:118px;top:33px;width:104px;height:55px;background:var(--teal)"></div>
    <div class="brand" style="left:134px;top:52px;color:var(--white);font-size:13px"><span class="c" style="width:9px;height:9px"></span>Corvane</div>
    <div class="abs" style="left:9px;top:96px;width:100px;font-size:4.6px;line-height:1.35;color:var(--teal)">Short intro on who we are, what we build and why our chips matter to clients.</div>
    <div class="abs tiny" style="left:128px;top:95px;width:94px">Our team designs mixed-signal parts for phones, cars and homes. We focus on power, speed and small size across every product line.</div>
    <div class="foot"><span class="dot"></span><span class="copy">© 2017 Corvane Semiconductor. All rights reserved</span><span class="sq"></span></div>
  </section>

  <!-- 8 icon slide -->
  <section class="slide">
    <div class="head">Icon Slide</div>
    <div class="photo" style="left:108px;top:0;right:0;bottom:0;background:linear-gradient(160deg,#3ab9d6,#1fa6c8 50%,#2c9fbc)" role="img" aria-label="Businessmen with umbrellas, tinted teal"></div>
    <div class="circle-ico" style="left:28px;top:32px;width:11px;height:11px;border:1px solid var(--teal)"><span style="width:5px;height:1px;background:var(--teal)"></span></div>
    <div class="circle-ico" style="left:28px;top:82px;width:11px;height:11px;background:var(--teal);color:var(--white);font-size:6px;font-weight:700">$</div>
    <div class="circle-ico" style="left:28px;top:126px;width:11px;height:11px;border:1px solid var(--teal)"><span style="width:4px;height:4px;border-radius:50%;border:1px solid var(--teal)"></span></div>
    <div class="abs" style="left:44px;top:32px;width:56px"><div style="font-size:3.8px;color:var(--teal)">Strategy</div><div class="tiny">Plan the next steps for growth and new markets.</div></div>
    <div class="abs" style="left:44px;top:82px;width:56px"><div style="font-size:3.8px;color:var(--teal)">Marketing</div><div class="tiny">Plan the next steps for growth and new markets.</div></div>
    <div class="abs" style="left:44px;top:126px;width:56px"><div style="font-size:3.8px;color:var(--teal)">Marketing</div><div class="tiny">Plan the next steps for growth and new markets.</div></div>
    <div class="circle-ico" style="left:102px;top:32px;width:12px;height:12px;background:var(--pink)"><span style="width:5px;height:4px;border:.8px solid var(--white)"></span></div>
    <div class="circle-ico" style="left:102px;top:82px;width:12px;height:12px;background:var(--pink)"><span style="width:4px;height:4px;border-radius:50%;border:.8px solid var(--white)"></span></div>
    <div class="circle-ico" style="left:102px;top:126px;width:12px;height:12px;background:var(--pink)"><span style="width:5px;height:5px;border-bottom:.8px solid var(--white);border-top:.8px solid var(--white)"></span></div>
    <div class="abs" style="left:119px;top:30px;width:60px"><div style="font-size:3.8px;color:var(--white)">Strategy</div><div class="tiny w">Plan the next steps for growth and new markets.</div></div>
    <div class="abs" style="left:119px;top:80px;width:60px"><div style="font-size:3.8px;color:var(--white)">Marketing</div><div class="tiny w">Plan the next steps for growth and new markets.</div></div>
    <div class="abs" style="left:119px;top:124px;width:60px"><div style="font-size:3.8px;color:var(--white)">Strategy</div><div class="tiny w">Plan the next steps for growth and new markets.</div></div>
    <div class="foot" style="right:130px"><span class="dot"></span></div>
  </section>

  <!-- 9 green section break -->
  <section class="slide" style="background:var(--green)">
    <div class="abs" style="left:160px;top:22px;width:110px;height:110px;border-radius:50%;background:rgba(255,255,255,.16)"></div>
    <svg class="abs" style="left:106px;top:72px" width="18" height="14" viewBox="0 0 18 14"><rect x="1" y="3" width="16" height="8" rx="4" fill="none" stroke="var(--white)" stroke-width="1"/><line x1="9" y1="3" x2="9" y2="11" stroke="var(--white)" stroke-width="1"/></svg>
    <div class="abs" style="left:0;right:0;top:91px;text-align:center;color:var(--white);font-size:8.5px;font-weight:600">Section Break</div>
    <div class="abs tiny w" style="left:78px;width:76px;top:103px;text-align:center">A short line to set up the next part of the talk and what comes after it.</div>
  </section>

  <!-- 10 purple section break -->
  <section class="slide" style="background:var(--purple)">
    <div class="abs" style="left:140px;top:8px;width:120px;height:120px;border-radius:50%;background:rgba(255,255,255,.14)"></div>
    <svg class="abs" style="left:105px;top:76px" width="18" height="14" viewBox="0 0 18 14"><rect x="1" y="3" width="16" height="8" rx="4" fill="none" stroke="var(--white)" stroke-width="1"/><line x1="9" y1="3" x2="9" y2="11" stroke="var(--white)" stroke-width="1"/></svg>
    <div class="abs" style="left:0;right:0;top:95px;text-align:center;color:var(--white);font-size:8.5px;font-weight:600">Section Break</div>
    <div class="abs tiny w" style="left:78px;width:76px;top:107px;text-align:center">A short line to set up the next part of the talk and what comes after it.</div>
  </section>

  <!-- 11 welcome strip -->
  <section class="slide">
    <div class="head">Your Title Here</div>
    <div class="photo" style="left:0;top:55px;width:74px;height:68px;background:linear-gradient(180deg,#9fb4c2,#4f6472)" role="img" aria-label="People walking past an office window"></div>
    <div class="abs" style="left:74px;top:55px;width:86px;height:68px;background:var(--teal);opacity:.92"></div>
    <svg class="abs" style="left:110px;top:72px" width="14" height="12" viewBox="0 0 14 12"><path d="M7 11 L1.5 5.5 A3 3 0 0 1 7 2.5 A3 3 0 0 1 12.5 5.5 Z" fill="none" stroke="var(--white)" stroke-width="1"/></svg>
    <div class="abs" style="left:74px;width:86px;top:89px;text-align:center;color:var(--white);font-size:4.5px">Welcome</div>
    <div class="abs tiny w" style="left:86px;width:62px;top:96px;text-align:center">A warm hello to all our new partners and staff.</div>
    <div class="photo" style="left:160px;top:55px;right:0;height:68px;background:linear-gradient(135deg,#cfd4d8,#5d6870 60%,#2d3337)" role="img" aria-label="Laptop showing charts on a desk"></div>
    <div class="foot"><span class="dot"></span><span class="copy">© 2017 Corvane Semiconductor. All rights reserved</span><span class="sq"></span></div>
  </section>

  <!-- 12 about us over photo -->
  <section class="slide">
    <div class="photo" style="inset:0;background:linear-gradient(120deg,#c7ccd0,#8e969c 40%,#5a5f63 70%,#b9c0c4)" role="img" aria-label="Two engineers studying a screen in a lab"></div>
    <div class="abs" style="left:125px;top:45px;right:0;height:80px;background:var(--teal);opacity:.93"></div>
    <div class="abs" style="left:133px;top:54px;color:var(--white);font-size:8.5px">About Us</div>
    <div class="abs tiny w" style="left:133px;top:68px;width:90px">We design chips that power the devices people use each day, with a focus on low power and high quality.</div>
    <div class="abs tiny w" style="left:133px;top:95px;width:90px">Our teams work across the world to bring new parts to market fast.</div>
    <div class="foot" style="left:180px"><span class="sq"></span></div>
  </section>

  <!-- 13 video -->
  <section class="slide">
    <div class="head">Your Title Goes Here</div>
    <div class="abs tiny" style="left:9px;top:32px;width:62px">Tell the story of the new deal and what it means for our clients.<br><br>Add key facts, dates and names here.<br><br>Keep each point short so it reads well on screen.<br><br>Close with the next step for the team.</div>
    <div class="abs" style="left:88px;top:33px;width:116px;height:72px;background:#2b2f33;border-radius:2px"></div>
    <div class="photo" style="left:91px;top:36px;width:110px;height:62px;background:linear-gradient(135deg,#dfe6ea,#a9bcc8 60%,#e9eef1)" role="img" aria-label="Presenter speaking in a video frame"></div>
    <div class="circle-ico" style="left:140px;top:61px;width:12px;height:12px;background:var(--teal)"><svg width="5" height="5" viewBox="0 0 5 5"><polygon points="1,0 5,2.5 1,5" fill="var(--white)"/></svg></div>
    <div class="abs" style="left:88px;top:105px;width:116px;height:5px;background:#d8dcdf"></div>
    <div class="abs" style="left:138px;top:110px;width:16px;height:7px;background:#c7ccd0"></div>
    <div class="abs" style="left:130px;top:117px;width:32px;height:1.5px;background:#b3b9bd"></div>
    <div class="foot"><span class="dot"></span><span class="copy">© 2017 Corvane Semiconductor. All rights reserved</span><span class="sq"></span></div>
  </section>

  <!-- 14 teal section break -->
  <section class="slide" style="background:var(--teal)">
    <div class="abs" style="left:135px;top:20px;width:110px;height:110px;border-radius:50%;background:rgba(255,255,255,.13)"></div>
    <div class="abs" style="left:27px;top:98px;width:11px;height:11px;border-radius:50%;background:var(--white)"></div>
    <div class="abs" style="left:27px;top:114px;color:var(--white);font-size:8.5px">Section Break</div>
    <div class="abs tiny w" style="left:27px;top:126px;width:90px">A short line to set up the next part of the talk and what comes after it.</div>
  </section>

  <!-- 15 quote with image -->
  <section class="slide">
    <div class="head">Title And Image + Text</div>
    <div class="photo" style="left:9px;top:32px;width:112px;height:55px;background:linear-gradient(180deg,#b8c7d1,#56687a)" role="img" aria-label="Commuters in a glass station hall"></div>
    <div class="abs" style="left:119px;top:32px;width:103px;height:55px;background:var(--teal)"></div>
    <div class="abs" style="left:124px;top:37px;color:var(--white);font-size:8px;font-weight:700">“</div>
    <div class="abs" style="left:132px;top:40px;width:84px;font-size:3.6px;line-height:1.35;color:var(--white)">This new step brings two strong teams together to build better chips.<br><span style="font-size:2.8px">— John Doe</span></div>
    <div class="abs" style="left:214px;top:72px;color:var(--white);font-size:8px;font-weight:700">”</div>
    <div class="abs tiny" style="left:9px;top:94px;width:213px">Add a few lines on the market, the products and the plan for the year ahead. Keep it clear and short.<br>Give the reader facts they can use, with dates and names where it helps.<br>End each part with one clear point so the team knows the next step.</div>
    <div class="foot"><span class="dot"></span><span class="copy">© 2017 Corvane Semiconductor. All rights reserved</span><span class="sq"></span></div>
  </section>

  <!-- 16 about us split -->
  <section class="slide">
    <div class="abs" style="left:128px;top:0;right:0;bottom:0;background:var(--teal);opacity:.85"></div>
    <div class="abs" style="left:160px;top:60px;width:70px;height:70px;border-radius:50%;background:rgba(255,255,255,.14)"></div>
    <div class="head" style="color:var(--teal)">About Us</div>
    <div class="photo" style="left:15px;top:30px;width:95px;height:58px;background:linear-gradient(160deg,#e8eef2,#a8bccb 60%,#6f8596)" role="img" aria-label="Man viewing a city skyline over rising charts"></div>
    <div class="abs tiny" style="left:9px;top:97px;width:110px">Share the history of the firm, our main sites and the products we sell to clients across the world today.</div>
    <div class="abs tiny w" style="left:138px;top:60px;width:76px">We have grown from a small team into a global maker of power and mixed-signal chips for many markets.</div>
    <div class="foot"><span class="dot"></span><span class="sq"></span></div>
  </section>

  <!-- 17 company details -->
  <section class="slide">
    <div class="head">Company Details</div>
    <div class="abs" style="left:13px;top:38px;width:98px;font-size:3.6px;color:var(--teal)">Key facts about our company</div>
    <div class="abs tiny" style="left:13px;top:45px;width:98px">Founded with one goal: make chips that save power.<br>• Offices in ten cities around the world.<br>• More than two thousand staff in teams.<br>• Products used in phones, cars and homes.<br>• Strong growth year after year.</div>
    <div class="abs" style="left:120px;top:45px;width:103px;height:62px;background:var(--teal)"></div>
    <div class="brand" style="left:136px;top:68px;color:var(--white);font-size:13px"><span class="c" style="width:9px;height:9px"></span>Corvane</div>
    <div class="foot"><span class="dot"></span><span class="copy">© 2017 Corvane Semiconductor. All rights reserved</span><span class="sq"></span></div>
  </section>

  <!-- 18 about us profile -->
  <section class="slide" style="background:var(--teal)">
    <div class="head white">About Us</div>
    <div class="photo" style="left:92px;top:34px;width:48px;height:48px;border-radius:50%;border:1.5px solid var(--white);background:radial-gradient(circle at 50% 40%,#d9c2b0,#8c7a6e 70%)" role="img" aria-label="Portrait of a team member"></div>
    <div class="abs tiny w" style="left:30px;width:171px;top:90px;text-align:center">A short profile of the person, their role and how they help our clients reach their goals each year.</div>
    <div class="abs tiny w" style="left:40px;width:151px;top:102px;text-align:center">Add a second line with a fun fact or a quote.</div>
    <div class="abs" style="left:101px;top:120px;display:flex;gap:5px"><span style="width:6px;height:6px;border-radius:50%;background:var(--white)"></span><span style="width:6px;height:6px;border-radius:50%;background:var(--white)"></span><span style="width:6px;height:6px;border-radius:50%;background:var(--white)"></span></div>
  </section>

  <!-- 19 blank -->
  <section class="slide">
    <div class="head">Your Blank Slide</div>
    <div class="foot"><span class="dot"></span><span class="copy">© 2017 Corvane Semiconductor. All rights reserved</span><span class="sq"></span></div>
  </section>

  <!-- 20 portfolio -->
  <section class="slide">
    <div class="abs" style="left:18px;top:18px;width:34px;height:14px;background:#2b2f33"></div>
    <div class="abs" style="left:72px;top:17px;width:36px;height:14px;border:1px solid #2b2f33"></div>
    <div class="abs" style="left:124px;top:15px;width:34px;height:18px;background:#5a5f63;clip-path:polygon(50% 0,100% 60%,100% 100%,0 100%,0 60%)"></div>
    <div class="abs" style="left:178px;top:12px;width:22px;height:22px;border-radius:50%;border:1.5px solid #2b2f33"></div>
    <div class="abs" style="left:18px;top:68px;width:34px;height:16px;border-top:1px solid #777;border-bottom:1px solid #777"></div>
    <div class="abs" style="left:70px;top:58px;width:93px;height:52px;background:var(--teal)"></div>
    <div class="abs" style="left:70px;width:93px;top:64px;text-align:center;color:var(--white);font-size:13px;font-weight:300;line-height:1.15">Our<br>Portfolio</div>
    <div class="abs" style="left:178px;top:62px;width:26px;height:26px;border-radius:50%;border:1px solid #2b2f33"></div>
    <div class="abs" style="left:15px;top:122px;width:40px;height:15px;border:1px dashed #777"></div>
    <div class="abs" style="left:70px;top:118px;width:34px;height:22px;background:#2b2f33"></div>
    <div class="abs" style="left:126px;top:120px;width:34px;height:18px;border:1px solid #2b2f33;border-radius:3px"></div>
    <div class="abs" style="left:178px;top:116px;width:24px;height:24px;border-radius:50%;border:1.5px solid #2b2f33"></div>
    <div class="tiny" style="position:absolute;left:90px;bottom:5px;font-size:2.4px">© 2017 Corvane Semiconductor</div>
  </section>

  <!-- 21 three bullets -->
  <section class="slide">
    <div class="head">Three Bullets Area</div>
    <div class="photo" style="left:0;right:0;top:27px;height:60px;background:linear-gradient(120deg,#f4f6f8,#d4dde4 50%,#a9b5be)" role="img" aria-label="Tablet, pen and papers on a desk"></div>
    <div class="circle-ico" style="left:41px;top:77px;width:18px;height:18px;background:var(--teal)"><span style="width:6px;height:6px;border-radius:50%;border:1px solid var(--white)"></span></div>
    <div class="circle-ico" style="left:107px;top:77px;width:18px;height:18px;background:var(--pink)"><span style="width:6px;height:6px;border:1px solid var(--white);transform:rotate(45deg)"></span></div>
    <div class="circle-ico" style="left:174px;top:77px;width:18px;height:18px;background:var(--green)"><span style="width:5px;height:7px;border:1px solid var(--white);border-radius:2px 2px 0 0"></span></div>
    <div class="abs tiny" style="left:20px;width:60px;top:99px;text-align:center">First key point with a short note to explain it.</div>
    <div class="abs tiny" style="left:86px;width:60px;top:99px;text-align:center">Second key point with a short note to explain it.</div>
    <div class="abs tiny" style="left:153px;width:60px;top:99px;text-align:center">Third key point with a short note to explain it.</div>
    <div class="foot"><span class="dot"></span><span class="copy">© 2017 Corvane Semiconductor. All rights reserved</span><span class="sq"></span></div>
  </section>

</main>
</body>
</html>
```